Label Design for honey from a small farm in Italy

We need a label for our Acacia's honey .
We are a little farm in Italy and we would like something like organic, raw and simple.
Maybe with botanical drawing with different color like watercolor o something like that (very important natural and easy)
the jar for 1kg of honey: Capacity: 780 ml - Height: 137 mm - Diameter: ∅ 94 mm
- size approx h 5,5 x 10/14cm ( we use the same label for kg and 500 gr jar)

Industry/Entity Type

Farm

Requirements
Must have
• the writings:
- Acacia
- Miele italiano di Acacia
- Da consumarsi preferibilmente entro: ( and below the space to put the date by the hands)
- some space to put some presentation of the farm or some phrases
- our logo
- the space to put the weight by the hands
- Prodotto da Azienda Agricola ...(produced by Farm Name and address....)
- Confezionato presso Apicoltura... (packaged at apiculture Name and address..)
- graphic of Acacia’s flowers ( like drawing)
Should not have
• Barcode
nutritional table

```html
<!DOCTYPE html>
<html lang="it">
<head>
<meta charset="utf-8">
<title>Acacia – Miele Italiano di Acacia – Etichetta</title>
<link href="https://fonts.googleapis.com/css2?family=Bodoni+Moda:wght@500&family=Oswald:wght@500&family=Barlow+Condensed:wght@600&display=swap" rel="stylesheet">
<style>
  :root {
    --backdrop: #d9d9db;
    --label-paper: #e4dde2;
    --paper-hex: #d8d0d6;
    --ink-black: #2a2a2a;
    --panel-dark: #2f302b;
    --honey-gold: #e1ab22;
    --gold-deep: #c98f14;
    --leaf-green: #5f7a3c;
    --blossom: #eeeeea;
    --white: #ffffff;
  }
  * { margin: 0; padding: 0; box-sizing: border-box; }
  html, body { width: 1200px; height: 1200px; overflow: hidden; }
  body { background: var(--backdrop); position: relative; }

  .label {
    position: absolute; left: 200px; top: 105px;
    width: 800px; height: 990px;
    background: radial-gradient(ellipse at 60% 40%, var(--label-paper), var(--paper-hex));
    overflow: hidden;
  }
  .botanical {
    position: absolute; left: 0; top: 20px; width: 235px; height: 970px;
    background:
      radial-gradient(ellipse at 40% 25%, var(--blossom) 0 30%, transparent 55%),
      radial-gradient(ellipse at 45% 70%, var(--leaf-green) 0 18%, transparent 50%),
      linear-gradient(180deg, #dcdcd2 0%, #a9b38e 55%, #6f8450 100%);
    opacity: .85;
  }
  .name-band {
    position: absolute; left: 226px; top: 308px; width: 144px; height: 425px;
    background: var(--ink-black);
    display: flex; align-items: center; justify-content: center;
    overflow: hidden;
  }
  .name-band h1 {
    writing-mode: vertical-rl;
    transform: rotate(180deg) scaleY(.78);
    font-family: "Bodoni Moda", serif; font-weight: 500;
    font-size: 100px; letter-spacing: 0; color: var(--white); line-height: 1;
    white-space: nowrap;
  }
  .subtitle-band {
    position: absolute; left: 370px; top: 308px; width: 68px; height: 425px;
    background: var(--honey-gold);
    display: flex; align-items: center; justify-content: center;
    overflow: hidden;
  }
  .subtitle-band h2 {
    writing-mode: vertical-rl; transform: rotate(180deg);
    font-family: "Oswald", sans-serif; font-weight: 500;
    font-size: 29px; color: var(--ink-black); letter-spacing: .5px; white-space: nowrap;
  }
  .info-panel {
    position: absolute; left: 444px; top: 308px; width: 326px; height: 425px;
    background: linear-gradient(180deg, var(--panel-dark) 0 59%, var(--honey-gold) 59% 100%);
    font-family: "Barlow Condensed", sans-serif; font-weight: 600; color: var(--ink-black);
  }
  .farm-name {
    position: absolute; top: 52px; left: 155px; transform: translateX(-50%);
    font-size: 22px; color: #cfd6d2; letter-spacing: .5px; white-space: nowrap;
  }
  .bee-emblem {
    position: absolute; left: 85px; top: 95px; width: 140px; height: 190px;
    background: radial-gradient(circle at 50% 40%, #f0c040, var(--gold-deep) 70%);
    clip-path: polygon(50% 0, 100% 20%, 100% 80%, 50% 100%, 0 80%, 0 20%);
  }
  .weight {
    position: absolute; right: 12px; top: 250px;
    display: flex; align-items: center; gap: 5px; font-size: 14px; color: var(--ink-black);
  }
  .weight-box { width: 22px; height: 28px; border: 1.5px solid var(--white); }
  .best-before {
    position: absolute; left: 12px; top: 388px; font-size: 15px; line-height: 1.25;
  }
  .producer {
    position: absolute; right: 12px; top: 388px; font-size: 15px; line-height: 1.25;
  }
</style>
</head>
<body>
  <div class="label">
    <div class="botanical" role="img" aria-label="Watercolour drawing of an acacia branch with white blossoms and green leaves"></div>

    <div class="name-band"><h1>ACACIA</h1></div>
    <div class="subtitle-band"><h2>MIELE ITALIANO DI ACACIA</h2></div>

    <div class="info-panel">
      <div class="farm-name">IL POGGETTO</div>
      <div class="bee-emblem" role="img" aria-label="Illustration of a bee on golden honeycomb cells"></div>
      <div class="weight"><span>WEIGHT:</span><span class="weight-box"></span></div>
      <p class="best-before">DA CONSUMARSI<br>PREFERIBILMENTE ENTRO:</p>
      <p class="producer">PRODOTTO DA AZIENDA AGRICOLA :</p>
    </div>
  </div>
</body>
</html>
```